Need posters that inspire entrepreneurs

I want to create beautiful, inspiring wall art. I'm looking for a designer to create an awesome sample (note this sample is not for real use). The winning design will form the foundation of our art "style" so there will be LOTS of ongoing work for the winning designer.

It's your challenge to create a style that is clean, inspiring and timeless, and possibly can be adapted to different colour palettes.

Looking for a perfect execution of words, image and design.

The attached example shows one idea. It should serve as an idea only.

Format of the images should be either rectangular or square. Exact size is preferably UK A4 (US letter) or max A3. Assume that a display would consist of a 4 x 4 image grid so size needs to allow for that in a small to medium size office.

The quotes I want in the 3 samples (each in an individual poster - not combined in 1 poster). Each quote should have it's own, the reason for three is to prove the design work on more than one quote. The quotes are:

1) Failure is the condiment that gives success its flavor.
– Dorian Welsby

2) Whether you think you can or think you can’t, you’re right.
– Oswald Pike

3) Ever tried. Ever failed. No matter. Try Again. Fail again. Fail better.
– Lionel Marwick

Each design should include the image of the person and the quote + any design elements you consider relevant. You should find relevant images of the individuals being quoted. The final images will not be published or used commercially in any way.

Font styles to use
Serif
Sans Serif

Colors

Designer to choose colors to be used in the design.

Requirements
Must have
• Words and headshot image - 1 per poster design.
• Please consider in the design that there will not always be photographs of the person quoted and as such the design will need to hold, whether the source is a photo, sketch or something else.
Nice to have
• None, but note that the final image will be printed on a wall mounted board, printed to the edge but not on the edge. The board will have black or white edges so consider in the design.
Should not have
• None

```html
<!DOCTYPE html>
<html lang="en">
<head>
<meta charset="utf-8">
<title>Quote Posters</title>
<link rel="stylesheet" href="https://fonts.googleapis.com/css2?family=Oswald:wght@500;600;700&family=Archivo+Narrow:wght@700&display=swap">
<style>
  :root {
    --page: #ffffff;
    --ink-black: #000000;
    --poster-white: #ffffff;
    --quote-red: rgba(140, 0, 0, 0.82);
    --quote-blue: #1c1670;
    --quote-blue-tint: #6a64c8;
    --quote-light: #e4dcdc;
    --byline-grey: #8a8a8a;
    --byline-dim: #6f6f6f;
    --photo-dark: #1a1a1a;
    --photo-mid: #5b5b5b;
    --photo-light: #a8a8a8;
  }
  * { margin: 0; padding: 0; box-sizing: border-box; }
  html, body {
    width: 860px; height: 1200px; overflow: hidden;
    background: var(--page);
  }
  .board { position: relative; width: 860px; height: 1200px; }
  .poster {
    position: absolute; overflow: hidden;
    box-shadow: 0 0 18px 6px rgba(0,0,0,0.12);
  }
  .poster--fail-better { left: 160px; top: 32px; width: 504px; height: 356px; background: var(--ink-black); }
  .poster--condiment { left: 160px; top: 424px; width: 496px; height: 352px; background: var(--poster-white); }
  .poster--think-you-can { left: 160px; top: 817px; width: 496px; height: 351px; background: var(--ink-black); }

  .portrait { position: absolute; z-index: 0; }
  .poster--fail-better .portrait {
    left: 0; top: 0; width: 360px; height: 356px;
    background: radial-gradient(ellipse 55% 60% at 38% 45%, var(--photo-light) 0%, var(--photo-mid) 40%, var(--photo-dark) 72%, var(--ink-black) 100%);
  }
  .poster--condiment .portrait {
    left: 250px; top: 14px; width: 246px; height: 338px;
    background: radial-gradient(ellipse 60% 62% at 55% 40%, var(--photo-mid) 0%, var(--photo-dark) 55%, rgba(26,26,26,0.6) 80%, rgba(255,255,255,0) 100%);
  }
  .poster--think-you-can .portrait {
    left: 210px; top: 0; width: 286px; height: 351px;
    background: radial-gradient(ellipse 50% 55% at 50% 25%, #4a4a4a 0%, #222 45%, var(--ink-black) 100%);
  }

  .quote-panel {
    position: absolute; z-index: 1; display: flex; align-items: center; justify-content: center;
    text-align: center; text-transform: uppercase;
    font-family: "Oswald", "Archivo Narrow", sans-serif; font-weight: 600;
  }
  .poster--fail-better .quote-panel {
    left: 194px; top: 50px; width: 310px; height: 264px;
    background: var(--quote-red); color: var(--quote-light);
    font-size: 29px; line-height: 37.5px; letter-spacing: 1.2px;
  }
  .poster--condiment .quote-panel {
    left: 0; top: 176px; width: 436px; height: 154px;
    background: var(--quote-blue); color: var(--poster-white);
    font-size: 32px; line-height: 40px; letter-spacing: 1.6px; padding-top: 6px;
  }
  .poster--condiment .quote-panel::before {
    content: ""; position: absolute; left: 0; top: 0; width: 150px; height: 22px;
    background: var(--quote-blue-tint); opacity: 0.75;
  }
  .poster--think-you-can .quote-panel {
    left: 0; top: 145px; width: 460px; height: 178px;
    background: var(--quote-red); color: var(--quote-light);
    font-size: 27px; line-height: 34px; letter-spacing: 1.3px;
  }
  .quote-panel p { position: relative; }

  .byline {
    position: absolute; z-index: 2; white-space: nowrap;
    font-family: "Archivo Narrow", sans-serif; font-weight: 700;
  }
  .poster--fail-better .byline { right: 16px; bottom: 14px; font-size: 13px; color: var(--byline-grey); }
  .poster--condiment .byline {
    left: 143px; top: 136px; font-size: 11px; color: var(--ink-black);
    text-transform: uppercase; letter-spacing: 0.4px;
  }
  .poster--think-you-can .byline { right: 38px; bottom: 2px; font-size: 17px; color: var(--byline-dim); }
</style>
</head>
<body>
  <main class="board">
    <section class="poster poster--fail-better">
      <div class="portrait" role="img" aria-label="Black and white portrait photo of Lionel Marwick"></div>
      <blockquote class="quote-panel"><p>Ever tried.<br>Ever failed.<br>No matter.<br>Try again.<br>Fail again.<br>Fail better.</p></blockquote>
      <span class="byline">Lionel Marwick</span>
    </section>

    <section class="poster poster--condiment">
      <div class="portrait" role="img" aria-label="Black and white portrait photo of Dorian Welsby seated"></div>
      <span class="byline">Dorian Welsby</span>
      <blockquote class="quote-panel"><p>Failure is the condiment<br>that gives success<br>its flavor</p></blockquote>
    </section>

    <section class="poster poster--think-you-can">
      <div class="portrait" role="img" aria-label="Dim black and white portrait photo of Oswald Pike"></div>
      <blockquote class="quote-panel"><p>Whether you think you can<br>or<br>think you can’t, you’re right</p></blockquote>
      <span class="byline">Oswald Pike</span>
    </section>
  </main>
</body>
</html>
```